"Wellenhafen" private practice for physiotherapy

we are looking for a flyer design for a private practice for physiotherapy. the name of the practice is "Wellenhafen".
Treatments such as: manual therapy, manual lymphatic drainage, classic massage, sectoral alternative practitioners are offered

The flyers should be double-sided and the format DIN long (105x210 mm)

Font styles to use
Serif

Colors
0094D4
00A9DD
6FCCEA
C7EBF8
E9F6FB

Requirements
Must have
• Wellenhafen, Lindenweg 17, 04719 Neustrand / Wellenhafen-praxis-beispiel.de / Tel. 03471 5820317

```html
<!DOCTYPE html>
<html lang="en">
<head>
<meta charset="utf-8">
<title>Wellenhafen Physiotherapy – DL Flyer</title>
<link rel="stylesheet" href="https://fonts.googleapis.com/css2?family=Poppins:wght@400;500;600;700;800;900&display=swap">
<style>
  :root {
    --blue: #0094D4;
    --blue-bright: #00A9DD;
    --blue-light: #6FCCEA;
    --blue-pale: #C7EBF8;
    --blue-mist: #E9F6FB;
    --navy: #0B4D77;
    --navy-deep: #133A57;
    --accent-cyan: #35E0E6;
    --ink: #0d0d0d;
    --stage: #e6e9ec;
    --white: #ffffff;
  }
  * { box-sizing: border-box; margin: 0; padding: 0; }
  html, body { width: 1200px; height: 800px; overflow: hidden; }
  body {
    background: var(--stage);
    font-family: "Poppins", sans-serif;
    display: flex; align-items: center; justify-content: center; gap: 60px;
  }
  .flyer {
    width: 340px; height: 680px; position: relative; overflow: hidden;
    box-shadow: 0 10px 30px rgba(0,0,0,.25);
  }

  /* Front */
  .front { background: var(--blue); }
  .front-arc { position: absolute; inset: 0 0 auto 0; width: 340px; height: 215px; }
  .front-title { position: absolute; top: 58px; left: 0; width: 100%; text-align: center; color: var(--white); }
  .front-title .brand { font-weight: 700; font-size: 31px; letter-spacing: 1px; line-height: 1; }
  .front-title .rule { width: 90px; height: 2px; background: var(--white); margin: 10px auto 8px; }
  .front-title .tagline { font-weight: 500; font-size: 19px; }
  .front-photo {
    position: absolute; top: 205px; left: 0; width: 340px; height: 345px;
    background: radial-gradient(ellipse at 60% 50%, #c9bfae 0%, #8e8a80 45%, #4d5250 100%);
  }
  .front-photo .ring { position: absolute; inset: 0; }
  .front-photo .headline {
    position: absolute; top: 140px; left: 0; width: 100%; text-align: center;
    font-weight: 900; font-size: 34px; color: #4a5258; letter-spacing: .5px;
  }
  .front-contact {
    position: absolute; top: 570px; left: 20px; width: 260px; text-align: center;
    color: var(--white); font-size: 12px; line-height: 1.4;
  }
  .front-contact .name { font-weight: 600; font-size: 14px; }
  .front-contact .tel { font-weight: 600; font-size: 12.5px; margin-top: 6px; }
  .front-corner { position: absolute; right: 0; bottom: 0; width: 85px; height: 85px; }

  /* Back */
  .back { background: var(--navy-deep); }
  .back-intro {
    height: 150px; padding: 30px 30px 0; text-align: center;
    color: var(--white); font-size: 13.5px; line-height: 1.3;
  }
  .back-services {
    position: absolute; top: 150px; left: 0; width: 340px; height: 385px;
    background: linear-gradient(180deg, #0a77b0 0%, #0a86c4 50%, #1a98d6 100%);
  }
  .back-services .mood {
    position: absolute; right: 0; top: 160px; width: 220px; height: 220px;
    background: radial-gradient(circle at 60% 50%, rgba(111,204,234,.35), rgba(111,204,234,0) 70%);
  }
  .services-heading {
    position: relative; text-align: center; color: var(--accent-cyan);
    font-weight: 500; font-size: 14px; line-height: 1.2; padding-top: 22px;
  }
  .services-heading .rule { width: 145px; height: 2px; background: var(--white); margin: 10px auto 0; }
  .service-list { position: relative; list-style: none; margin-top: 22px; padding-left: 28px; }
  .service-item { display: flex; align-items: center; gap: 14px; height: 72px; }
  .service-icon {
    width: 58px; height: 58px; border-radius: 50%; background: var(--navy-deep);
    flex: none; display: flex; align-items: center; justify-content: center;
  }
  .service-name { color: var(--white); font-weight: 600; font-size: 15px; line-height: 1.15; }
  .booking {
    position: absolute; top: 535px; left: 0; width: 340px; height: 70px;
    background: var(--white); padding: 10px 0 0 32px; color: var(--ink);
  }
  .booking .prompt { font-weight: 500; font-size: 12px; letter-spacing: .3px; }
  .booking .phone { display: flex; align-items: center; gap: 8px; font-weight: 700; font-size: 28px; line-height: 1.15; }
  .back-brand {
    position: absolute; top: 605px; left: 0; width: 340px; height: 75px;
    display: flex; align-items: center; justify-content: center;
    color: var(--white); font-weight: 700; font-size: 32px;
  }
</style>
</head>
<body>

  <section class="flyer front" aria-label="Flyer front">
    <svg class="front-arc" viewBox="0 0 340 215" aria-hidden="true">
      <circle cx="170" cy="-50" r="265" fill="var(--navy)"/>
      <circle cx="155" cy="-75" r="240" fill="var(--blue)"/>
    </svg>
    <div class="front-title">
      <div class="brand">WELLENHAFEN</div>
      <div class="rule"></div>
      <div class="tagline">Physiotherapy</div>
    </div>
    <div class="front-photo" role="img" aria-label="Photo of a runner on a misty tree-lined path">
      <svg class="ring" viewBox="0 0 340 345" aria-hidden="true">
        <circle cx="175" cy="180" r="150" fill="none" stroke="rgba(11,77,119,.35)" stroke-width="14"/>
      </svg>
      <div class="headline">PHYSIOTHERAPY</div>
    </div>
    <div class="front-contact">
      <div class="name">Wellenhafen,</div>
      <div>Lindenweg 17,</div>
      <div>04719 Neustrand</div>
      <div>Wellenhafen-praxis-beispiel.de</div>
      <div class="tel">Tel. 03471 5820317</div>
    </div>
    <svg class="front-corner" viewBox="0 0 85 85" aria-hidden="true">
      <circle cx="95" cy="95" r="75" fill="none" stroke="var(--navy)" stroke-opacity=".6" stroke-width="13"/>
      <circle cx="95" cy="95" r="50" fill="none" stroke="var(--navy)" stroke-opacity=".45" stroke-width="10"/>
    </svg>
  </section>

  <section class="flyer back" aria-label="Flyer back">
    <p class="back-intro">Wellenhafen understand that you have individual needs and we will make your treatment plan so that it is specific to you.</p>
    <div class="back-services">
      <div class="mood" role="img" aria-label="Photo of a person stretching on an exercise ball"></div>
      <div class="services-heading">
        We offer specialist care<br>in the following area's;
        <div class="rule"></div>
      </div>
      <ul class="service-list">
        <li class="service-item">
          <span class="service-icon"><svg width="28" height="28" viewBox="0 0 28 28" aria-hidden="true"><rect x="3" y="17" width="22" height="4" rx="2" fill="#fff"/><circle cx="17" cy="8" r="3.5" fill="#fff"/></svg></span>
          <span class="service-name">Manual Therapy</span>
        </li>
        <li class="service-item">
          <span class="service-icon"><svg width="28" height="28" viewBox="0 0 28 28" aria-hidden="true"><circle cx="14" cy="14" r="9" fill="none" stroke="#fff" stroke-width="2.5"/><circle cx="14" cy="14" r="3" fill="#fff"/></svg></span>
          <span class="service-name">Manual Lymphatic<br>Drainage</span>
        </li>
        <li class="service-item">
          <span class="service-icon"><svg width="28" height="28" viewBox="0 0 28 28" aria-hidden="true"><rect x="3" y="18" width="22" height="4" rx="2" fill="#fff"/><circle cx="8" cy="10" r="3.5" fill="#fff"/></svg></span>
          <span class="service-name">Classic Massage</span>
        </li>
        <li class="service-item">
          <span class="service-icon"><svg width="28" height="28" viewBox="0 0 28 28" aria-hidden="true"><path d="M14 23 C4 15 4 7 9.5 6.5 C12 6.3 13.3 8 14 9.5 C14.7 8 16 6.3 18.5 6.5 C24 7 24 15 14 23Z" fill="#fff"/><path d="M14 11v6M11 14h6" stroke="var(--navy-deep)" stroke-width="2"/></svg></span>
          <span class="service-name">Sectoral Alternative<br>Practitioner</span>
        </li>
      </ul>
    </div>
    <div class="booking">
      <div class="prompt">BOOK YOUR APPONTMENT TODAY ON</div>
      <div class="phone">
        <svg width="20" height="20" viewBox="0 0 24 24" aria-hidden="true"><path d="M6.6 10.8a15.1 15.1 0 0 0 6.6 6.6l2.2-2.2a1 1 0 0 1 1-.25 11.4 11.4 0 0 0 3.6.57 1 1 0 0 1 1 1V20a1 1 0 0 1-1 1A17 17 0 0 1 3 4a1 1 0 0 1 1-1h3.5a1 1 0 0 1 1 1c0 1.250.2 2.450.57 3.57a1 1 0 0 1-.25 1z" fill="var(--ink)"/></svg>
        03471 5820317
      </div>
    </div>
    <div class="back-brand">Wellenhafen</div>
  </section>

</body>
</html>
```